Brell Harbor Company Business Cards

Front and Back Business Card - logo and text setup - cool design. I need workable photoshop or illustrator files so I can setup each employee card with design that is created
Updates

Hi everyone, thank you for the great entries. Please no more white and blue cards - there are so many already - black and silver only now please. thanks!

Target Market(s)

Construction Industry - Facility Managers

Industry/Entity Type

Construction

Contact Information for Business Card

I really like contemporary simplistic looks - clean neat....not opposed to seeing some black backrounds

Requirements
Must have
• Logo/website address with design on front only - www.brellharbor-example.com (logo attached)
• Back:
• Name/Title/Company Address/Phone/email address
Nice to have
• Cool design
Should not have
• Nothing gimmicky like Fire or Water - since we are a Fire Protection company - it has all been done

```html
<!DOCTYPE html>
<html lang="en">
<head>
<meta charset="utf-8">
<title>Brell Harbor Company Business Cards</title>
<link rel="stylesheet" href="https://fonts.googleapis.com/css2?family=Open+Sans:wght@400;700;800&display=swap">
<style>
  :root {
    --backdrop: #6f7277;
    --silver-light: #eceef0;
    --silver: #c7cad0;
    --silver-mid: #9a9ea5;
    --silver-dark: #6b6f76;
    --black: #111214;
    --black-soft: #2a2c30;
    --ink: #1b1c1f;
  }
  * { box-sizing: border-box; margin: 0; padding: 0; }
  html, body {
    width: 1200px; height: 1023px; overflow: hidden;
    background: var(--backdrop);
    font-family: "Open Sans", Arial, sans-serif;
  }
  .stage { position: relative; width: 1200px; height: 1023px; }

  .card {
    position: absolute;
    width: 560px; height: 320px;
    box-shadow: 0 6px 18px rgba(0,0,0,0.3);
  }

  /* Contact side */
  .card--contact {
    left: 80px; top: 110px;
    background: linear-gradient(135deg, var(--silver-light), var(--silver));
    color: var(--ink);
  }
  .brand-lockup {
    position: absolute; left: 34px; top: 140px;
    display: flex; align-items: center; gap: 10px;
  }
  .brand-lockup__square { width: 14px; height: 14px; background: var(--black); }
  .brand-lockup__name {
    font-weight: 800; font-size: 30px; color: var(--black); letter-spacing: -0.5px;
  }
  .divider {
    position: absolute; left: 268px; top: 40px; width: 0; height: 240px;
    border-left: 3px dashed var(--silver-mid);
  }
  .contact { position: absolute; left: 300px; top: 38px; }
  .contact__name { font-weight: 700; font-size: 19px; color: var(--black); line-height: 1.2; }
  .contact__title { font-size: 13px; color: var(--silver-dark); margin-bottom: 22px; }
  .contact__address { font-size: 13px; line-height: 1.45; margin-bottom: 20px; }
  .contact__list { list-style: none; font-size: 13px; line-height: 1.6; }
  .contact__list li { display: flex; align-items: center; gap: 8px; }
  .contact__icon { width: 13px; height: 13px; flex: none; color: var(--silver-dark); }

  /* Brand side */
  .card--brand {
    left: 560px; top: 590px;
    background: linear-gradient(135deg, var(--black), var(--black-soft));
  }
  .brand-mark {
    position: absolute; left: 0; right: 0; top: 118px;
    display: flex; justify-content: center; align-items: center; gap: 14px;
  }
  .brand-mark__square { width: 20px; height: 20px; background: var(--silver); }
  .brand-mark__name {
    font-weight: 800; font-size: 46px; color: var(--silver); letter-spacing: -1px;
  }
  .brand-url {
    position: absolute; left: 34px; bottom: 30px;
    font-size: 14px; color: var(--silver);
  }
</style>
</head>
<body>
<main class="stage">

  <section class="card card--contact" aria-label="Business card contact side">
    <div class="brand-lockup">
      <span class="brand-lockup__square"></span>
      <span class="brand-lockup__name">Brell Harbor</span>
    </div>
    <div class="divider"></div>
    <div class="contact">
      <p class="contact__name">Dana Morrow</p>
      <p class="contact__title">Director</p>
      <p class="contact__address">48 Quarry Lane<br>Westford Bay, NY 10990</p>
      <ul class="contact__list">
        <li>
          <svg class="contact__icon" viewBox="0 0 16 16" aria-hidden="true"><path fill="currentColor" d="M3 1l3 3-1.5 2a9 9 0 0 0 5.5 5.5L12 10l3 3-2 2C6 15 1 10 1 3z"/></svg>
          (555) 014-2290
        </li>
        <li>
          <svg class="contact__icon" viewBox="0 0 16 16" aria-hidden="true"><rect x="4" y="1" width="8" height="5" fill="currentColor"/><rect x="1" y="6" width="14" height="7" rx="1" fill="currentColor"/><rect x="4" y="10" width="8" height="5" fill="#eceef0" stroke="currentColor"/></svg>
          (555) 014-2291
        </li>
        <li>
          <svg class="contact__icon" viewBox="0 0 16 16" aria-hidden="true"><rect x="1" y="3" width="14" height="10" fill="currentColor"/><path d="M1 3l7 6 7-6" fill="none" stroke="#eceef0" stroke-width="1.4"/></svg>
          info@brellharbor-example.com
        </li>
        <li>
          <svg class="contact__icon" viewBox="0 0 16 16" aria-hidden="true"><circle cx="8" cy="8" r="7" fill="currentColor"/><path d="M1 8h14M8 1c-3 3-3 11 0 14M8 1c3 3 3 11 0 14" fill="none" stroke="#eceef0" stroke-width="1"/></svg>
          www.brellharbor-example.com
        </li>
      </ul>
    </div>
  </section>

  <section class="card card--brand" aria-label="Business card brand side">
    <div class="brand-mark">
      <span class="brand-mark__square"></span>
      <span class="brand-mark__name">Brell Harbor</span>
    </div>
    <p class="brand-url">www.brellharbor-example.com</p>
  </section>

</main>
</body>
</html>
```